IT Consulting Site Revamping for Marlune

I've put a skeleton together on my website, but realize I need some help (it's http://pilot.marlune-example.ca).
I've pulled together tidbits from other websites, but really need my site to be cleaned up, and really spruced up.
I primarily focus on the IT needs of small to medium size businesses, taking care of everything from their servers and networks down to their workstations.
I also want a page listing the vendors (and logos) that I work with including Quillsoft, Zentrix, Halvor, Brax, TL, RZO, VELK, Trevo, Gatemoor.
There should also be a simple form to get a quote that will email me.
The final design should communicate strength and reliability.
I would like this to be a fully functional website, that I can upload to Plumly Pages, with the same sort of pages that are existing on http://pilot.marlune-example.ca
Updates
Hey everyone,
Hi everyone,
Reason: Hi all,
There are some designers that would like to submit some new designs, so I'm extending the deadline.
Thanks,
Target Market(s)
Small to medium size business owners. This will primarily be males who work in the oil and gas industry.
Industry/Entity Type
Consulting
Look and feel
Each slider illustrates characteristics of the customer's brand and the style your logo design should communicate.

```html
<!DOCTYPE html>
<html lang="en">
<head>
<meta charset="utf-8">
<title>Marlune Solutions</title>
<link href="https://fonts.googleapis.com/css2?family=Carlito:wght@400;700&display=swap" rel="stylesheet">
<style>
:root{
  --page:#ececec;
  --blue:#2a78b8;
  --blue-dark:#22629a;
  --panel:#c4d6e2;
  --card:#e1e1e1;
  --text:#4a4a4a;
  --heading:#555;
  --grey-btn:#6a8197;
  --green:#43a72c;
  --orange:#e4511c;
  --brown:#8a5518;
  --footer:#c4d3dd;
}
*{margin:0;padding:0;box-sizing:border-box}
html,body{width:1085px;height:1200px;overflow:hidden}
body{background:var(--page);font-family:"Carlito",sans-serif;color:var(--text);position:relative}
.abs{position:absolute}
.brand{left:148px;top:30px;display:flex;align-items:center;gap:10px}
.brand-mark{width:42px;height:42px;border-radius:50%;background:var(--blue)}
.brand-name{font-size:38px;font-weight:700;color:var(--blue);line-height:1}
.brand-sub{font-size:11px;letter-spacing:6px;color:var(--blue);margin-top:2px}
.nav{left:140px;top:112px;width:805px;height:41px;background:linear-gradient(#e4e4e4,#c9c9c9);border-bottom:3px solid var(--blue)}
.nav-item{position:absolute;top:0;height:38px;line-height:40px;font-size:14.5px;font-weight:700;color:var(--blue);transform:translateX(-50%);white-space:nowrap}
.nav-item.active{left:191px;width:118px;transform:none;background:var(--blue);color:#fff;text-align:center}
.dropdown{left:331px;top:153px;width:223px;height:169px;background:var(--blue);border-bottom:3px solid #fff;list-style:none;padding-top:12px}
.dropdown li{color:#fff;font-size:13.5px;height:30.3px;padding-left:15px;text-transform:uppercase}
.hero{left:140px;top:193px;width:805px;height:266px;background:var(--panel);border-bottom:3px solid var(--blue)}
.hero-photo{position:absolute;left:0;top:0;width:411px;height:263px;background:linear-gradient(135deg,#e8eef5,#9fb4c8 55%,#5d7389)}
.hero-caption{position:absolute;left:0;top:154px;width:397px;height:72px;background:rgba(74,124,170,.85);border-radius:0 0 4px 0;padding:14px 14px;color:#fff;font-weight:700;font-size:17px;line-height:22px}
.c-easy{color:#c8ea4a}.c-aff{color:#f59a3a}.c-rel{color:#f3ec72}
.about{position:absolute;left:415px;top:22px;width:375px;font-size:12.2px;line-height:16.3px;color:#3c3c3c}
.about h2{font-size:14.5px;font-weight:700;color:#444;margin-bottom:8px}
.about h2 span{color:var(--blue)}
.about p{margin-bottom:16px}
.btn{display:block;text-align:center;color:#fff;font-size:11px;border-radius:3px;height:22px;line-height:22px}
.about .btn{width:166px;background:linear-gradient(#3a85c4,var(--blue-dark));border:1px solid #1f5888;margin-top:2px}
.section-title{left:139px;width:806px;font-size:15.5px;color:#444;border-bottom:3px solid var(--blue);padding-bottom:2px}
.card{position:absolute;top:530px;width:145px;height:356px;background:var(--card);text-align:center}
.card-icon{height:144px;border-bottom:1px solid #c8c8c8;display:flex;align-items:center;justify-content:center}
.icon-fill{width:120px;height:110px;border-radius:6px}
.i-grey{background:linear-gradient(#c2ccd6,#a7b5c3)}
.i-green{background:linear-gradient(#b9dcae,#9fcd91)}
.i-orange{background:linear-gradient(#f2c0a8,#eca685)}
.i-brown{background:linear-gradient(#d3bb9c,#c2a27c)}
.i-blue{background:linear-gradient(#adc6dd,#8fb1d0)}
.card h3{font-size:15px;line-height:21px;color:#555;margin-top:17px;text-transform:uppercase}
.card p{font-size:12px;line-height:16.2px;color:#555;margin:14px 6px 0}
.card .btn{position:absolute;left:10px;top:319px;width:127px}
.b-grey{background:linear-gradient(#7d94a9,var(--grey-btn))}
.b-green{background:linear-gradient(#53bb39,var(--green))}
.b-orange{background:linear-gradient(#f06530,var(--orange))}
.b-brown{background:linear-gradient(#9c6426,var(--brown))}
.b-blue{background:linear-gradient(#3a85c4,var(--blue-dark))}
.vendor{position:absolute;top:976px;width:145px;height:140px;background:radial-gradient(#f6f6f6,#dedede);border:1px solid #d4d4d4;display:flex;align-items:center;justify-content:center;gap:6px;font-size:21px;font-weight:700;color:#555}
.dot{width:14px;height:14px;background:var(--blue)}
.dot.round{border-radius:50%}
.footer{left:140px;top:1155px;width:805px;height:25px;background:var(--footer);font-size:10.5px;line-height:25px;padding:0 9px 0 14px;display:flex;justify-content:space-between;color:#444}
</style>
</head>
<body>
<header class="brand abs">
  <span class="brand-mark"></span>
  <div><div class="brand-name">Marlune</div><div class="brand-sub">solutions</div></div>
</header>

<nav class="nav abs">
  <span class="nav-item" style="left:108px">HOME</span>
  <span class="nav-item active">OUR SERVICES</span>
  <span class="nav-item" style="left:393px">ABOUT US</span>
  <span class="nav-item" style="left:536px">OUR PRODUCTS</span>
  <span class="nav-item" style="left:678px">CONTACT US</span>
</nav>

<section class="hero abs">
  <div class="hero-photo" role="img" aria-label="Two IT technicians working in a server room"></div>
  <div class="hero-caption">Small Business Information Technology Services<br><span class="c-easy">Easy,</span> <span class="c-aff">Affordable</span> and <span class="c-rel">Reliable.</span></div>
  <div class="about">
    <h2>About <span>Marlune Solutions</span></h2>
    <p>Marlune Solutions is a computer solutions provider and IT consulting firm that supports a wide variety of local small businesses in the Calgary area primarily. Our company also provides IT services to businesses throughout Alberta on special projects.</p>
    <p>Marlune has been trusted for over the last 7 years by small business companies like yours. Whether you are looking for an ongoing computer support company, looking to outsource your small business computer work, or just looking for a computer company to help you solve a computer problem, Marlune is your right choice.</p>
    <a class="btn">read more about us</a>
  </div>
</section>

<ul class="dropdown abs">
  <li>Managed IT Services</li>
  <li>Storage and Virtualization</li>
  <li>Networking Services</li>
  <li>Backup and Recovery</li>
  <li>Computer Repair Service</li>
</ul>

<h2 class="section-title abs" style="top:492px;font-weight:400">Our Services</h2>

<article class="card" style="left:139px">
  <div class="card-icon"><div class="icon-fill i-grey" role="img" aria-label="Illustration of a monitor circled by rotating arrows"></div></div>
  <h3>Managed IT<br>Services</h3>
  <p>Lorem ipsum dolor sit amet, consectetur adipiscing elit. Nunc vulputate pretium vehicula. Ut a tristique magna.</p>
  <a class="btn b-grey">more about it</a>
</article>
<article class="card" style="left:305px">
  <div class="card-icon"><div class="icon-fill i-green" role="img" aria-label="Illustration of a monitor exchanging data with a storage drum"></div></div>
  <h3>Storage and<br>Virtualization</h3>
  <p>Lorem ipsum dolor sit amet, consectetur adipiscing elit. Nunc vulputate pretium vehicula. Ut a tristique magna.</p>
  <a class="btn b-green">more about it</a>
</article>
<article class="card" style="left:470px">
  <div class="card-icon"><div class="icon-fill i-orange" role="img" aria-label="Illustration of three networked computers"></div></div>
  <h3>Networking<br>Services</h3>
  <p>Lorem ipsum dolor sit amet, consectetur adipiscing elit. Nunc vulputate pretium vehicula. Ut a tristique magna.</p>
  <a class="btn b-orange">more about it</a>
</article>
<article class="card" style="left:635px">
  <div class="card-icon"><div class="icon-fill i-brown" role="img" aria-label="Illustration of a server stack backing up a monitor"></div></div>
  <h3>Backup and<br>Recovery</h3>
  <p>Lorem ipsum dolor sit amet, consectetur adipiscing elit. Nunc vulputate pretium vehicula. Ut a tristique magna.</p>
  <a class="btn b-brown">more about it</a>
</article>
<article class="card" style="left:799px">
  <div class="card-icon"><div class="icon-fill i-blue" role="img" aria-label="Illustration of crossed repair tools"></div></div>
  <h3>Computer<br>Rerpair Services</h3>
  <p>Lorem ipsum dolor sit amet, consectetur adipiscing elit. Nunc vulputate pretium vehicula. Ut a tristique magna.</p>
  <a class="btn b-blue">more about it</a>
</article>

<h2 class="section-title abs" style="top:921px;font-weight:400">Vendors</h2>

<svg class="abs" style="left:106px;top:1030px" width="18" height="28" viewBox="0 0 18 28"><path d="M14 3L4 14l10 11" fill="none" stroke="#2f6fa8" stroke-width="4"/></svg>
<div class="vendor" style="left:139px"><span class="dot"></span>Quillsoft</div>
<div class="vendor" style="left:305px">Zentrix</div>
<div class="vendor" style="left:470px;color:#111">Halvor</div>
<div class="vendor" style="left:635px;color:var(--blue)"><span class="dot round"></span>Brax</div>
<div class="vendor" style="left:799px;color:#1a5c9c"><span class="dot round" style="background:#1a5c9c"></span>TL</div>
<svg class="abs" style="left:963px;top:1030px" width="18" height="28" viewBox="0 0 18 28"><path d="M4 3l10 11L4 25" fill="none" stroke="#2f6fa8" stroke-width="4"/></svg>

<footer class="footer abs"><span>2012 © Marlune Solutions</span><span>All Rights Reserved</span></footer>
</body>
</html>
```